Flyer Design Project

I teach a spiritual dance class and I want to explain what it is and who it would benefit. I would love to have a sticker for where I am teaching it because that can change.

I want it to be a bit spiritual, very hip and cool, and transformational!!

Target Market(s)

Mostly women (or enlightened men)! all ages

Requirements
Must have
• Tidal Sway

We need to move. We need to breathe. We need to smile and giggle and laugh and cry and scream and make noise and dance. It's not about burning calories and it is not about reaching a goal. It's about feeling. It's about taking the time to nurture our souls. It's about finding joy and peace in our hectic lives. It's about healing.

Tidal Sway is a wildly fun, uplifting, emotionally cleansing, refreshing, restorative, heart-opening, transformational dance celebration that is sure to leave you relaxed and smiling. All ages, shapes and sizes are welcome with no experience necessary.
About Nora:

I was certified at Venduro in both “Move Through Morning” and “Orbit Motion” and am a
certified Group Exercise Instructor with the Cardio and Wellness Guild of Northland (CWGN). I also have a black belt in Tae Kwon Do. As of 2013, I will be a certified holistic health and nutrition coach and am the creator of the popular Bright, Brisk, and Bold page on Chatterbook.
For more info:
Noradekker@mailquill.com

Classes and workshops to energize your body, mind, and spirit.

```html
<!DOCTYPE html>
<html lang="en">
<head>
<meta charset="utf-8">
<title>Tidal Sway Flyer</title>
<link rel="stylesheet" href="https://fonts.googleapis.com/css2?family=Open+Sans:wght@400;600;700;800&display=swap">
<style>
  :root {
    --sky-top: #1d3340;
    --sky-mid: #3f6570;
    --sky-glow: #b7a77c;
    --grass: #4d5a2a;
    --orange-light: #f6b33a;
    --orange-deep: #e48d1f;
    --white: #ffffff;
    --navy: #16303d;
    --frame: rgba(255,255,255,0.85);
  }
  * { box-sizing: border-box; margin: 0; padding: 0; }
  html, body { width: 849px; height: 1200px; overflow: hidden; }
  body { font-family: "Open Sans", Arial, sans-serif; color: var(--white); }
  .flyer {
    position: relative; width: 849px; height: 1200px; overflow: hidden;
    background: linear-gradient(180deg, var(--orange-light) 0%, var(--orange-deep) 100%);
  }
  .hero-photo {
    position: absolute; left: 0; top: 0; width: 849px; height: 525px;
    background:
      linear-gradient(180deg, rgba(0,0,0,0) 70%, var(--grass) 100%),
      radial-gradient(ellipse at 65% 80%, var(--sky-glow) 0%, rgba(183,167,124,0) 45%),
      linear-gradient(180deg, var(--sky-top) 0%, var(--sky-mid) 70%, #6d7a5c 100%);
  }
  .title {
    position: absolute; left: 110px; top: 48px;
    font-size: 74px; font-weight: 800; letter-spacing: -1px; line-height: 1;
  }
  .intro {
    position: absolute; left: 93px; top: 190px; width: 380px;
    font-size: 16.5px; line-height: 1.38; font-weight: 600;
  }
  .description {
    position: absolute; left: 93px; top: 562px; width: 470px;
    font-size: 16px; line-height: 1.42;
  }
  .description strong { font-weight: 700; }
  .portrait {
    position: absolute; left: 586px; top: 553px; width: 215px; height: 217px;
    border: 4px solid var(--white);
    background: linear-gradient(160deg, #c9a27a 0%, #8a4a3a 55%, #c8463f 100%);
  }
  .contact {
    position: absolute; right: 48px; top: 782px; text-align: right;
    font-size: 15px; line-height: 1.35;
  }
  .bio {
    position: absolute; left: 90px; top: 843px; width: 711px; height: 162px;
    border: 1.5px solid var(--frame);
    padding: 20px 24px; font-size: 15px; line-height: 1.5;
  }
  .bio p + p { margin-top: 2px; }
  .footer-band {
    position: absolute; left: 0; top: 1110px; width: 849px; height: 50px;
    background: var(--navy);
    display: flex; align-items: center; justify-content: center;
    font-size: 21px; letter-spacing: 4px; font-weight: 600;
  }
</style>
</head>
<body>
<main class="flyer">
  <div class="hero-photo" role="img" aria-label="Woman dancing with arms flung back in a grassy field under a dusky teal sky"></div>
  <h1 class="title">Tidal Sway</h1>
  <p class="intro">We need to move. We need to breathe. We need to smile and giggle and laugh and cry and scream and make noise and dance. It's not about burning calories and it is not about reaching a goal. It's about feeling. It's about taking the time to nurture our souls. It's about finding joy and peace in our hectic lives. It's about healing.</p>

  <p class="description"><strong>Tidal Sway</strong> is a wildly fun, uplifting, emotionally cleansing, refreshing, restorative, heart-opening, transformational dance celebration that is sure to leave you relaxed and smiling. All ages, shapes and sizes are welcome with no experience necessary.</p>

  <div class="portrait" role="img" aria-label="Portrait of the instructor, Nora"></div>

  <div class="contact">
    <div>Email Noradekker@mailquill.com</div>
    <div>Phone 555.010.4821</div>
  </div>

  <section class="bio">
    <p>I was certified at Venduro in both “Move Through Morning” and “Orbit Motion” and am a certified Group Exercise Instructor with the Cardio and Wellness Guild of Northland (CWGN).</p>
    <p>I also have a black belt in Tae Kwon Do. As of 2013, I will be a certified holistic health and nutrition coach and am the creator of the popular Bright, Brisk, and Bold page on Chatterbook.</p>
  </section>

  <footer class="footer-band">WWW.TIDALSWAYDANCE.COM</footer>
</main>
</body>
</html>
```